Willowmere Spa and Beauty Ltd. (Name of business)

I need a business card designed for this new company based out of Toronto Ontario. We specialize in Eyelash Extensions, Manicures and Pedicures, body waxing, massages, laser hair removal and Injectable treatments. Also offer a variety of products for sale, such as skin cream serums, collagen gel, eye cream, etc. It is a safe relaxing and non-judgemental environnment. Clients are welcome to come be pampered for the half or full day. Many service packages to choose from.

Open 7days per week from 8am to 8pm.

Marissa Thornbury
Spa Facilitator
Willowmere Spa and Beauty Ltd.
7200 Calder Ave; Suite 1400
Toronto ON K8P 2W7

OFFICE: 416.739.4100
FAX: 416.739.4101
CELL: 416.582.6074
EMAIL: marissa.thornbury@willowmerespa.example

Target Market(s)

Target market is primarily female ranging from 16 years old to 50 years old.

Industry/Entity Type

Business

Contact Information for Business Card

Marissa Thornbury
Spa Facilitator
7200 Calder Ave; Suite 1400
Toronto ON K8P 2W7

OFFICE: 416.739.4100
FAX: 416.739.4101
CELL: 416.582.6074

Logo Text

I dont have a logo yet. I would like it simple but sophisticated and modern.

Font styles to use
Serif

Requirements
Must have
• all pertinent details such as company name, logo, name and contact information, services that are offered, including package rates
Nice to have
• Company name and logo prominent. A card that is neat and the information such as address, phone number, fax, email, etc is not too crowded but laid out in an easy to read format.
• Possibly on the back of card - some of the services offered could be listed, as well as professional cream lotions and serums. Hours of operation etc.

```html
<!DOCTYPE html>
<html lang="en">
<head>
<meta charset="utf-8">
<title>Willowmere Spa and Beauty Ltd. — Card Back</title>
<link rel="stylesheet" href="https://fonts.googleapis.com/css2?family=Quicksand:wght@300;400&display=swap">
<style>
  :root {
    --ink: #0e131b;
    --gold: #d6bc63;
    --gold-deep: #a8873a;
    --gold-light: #f1e09a;
    --text: #ecebe6;
    --rule-edge: #ffffff;
  }
  * { margin: 0; padding: 0; box-sizing: border-box; }
  html, body { width: 1200px; height: 687px; overflow: hidden; background: var(--ink); }
  .card {
    position: relative;
    width: 1200px;
    height: 687px;
    background: var(--ink);
    font-family: "Quicksand", sans-serif;
    font-weight: 300;
  }
  .rule {
    position: absolute;
    height: 3px;
    background: linear-gradient(90deg, var(--rule-edge) 0%, var(--gold) 30%, var(--gold-light) 60%, var(--gold) 80%, var(--rule-edge) 100%);
  }
  .rule--top { left: 31px; width: 1139px; top: 64px; }
  .rule--mid { left: 35px; width: 1140px; top: 557px; }
  .rule--bottom { left: 35px; width: 1140px; top: 633px; }

  .brand {
    position: absolute;
    left: 60px;
    top: 171px;
    width: 440px;
    text-align: center;
    color: var(--gold);
  }
  .brand__mark { display: block; margin: 0 auto 44px; }
  .brand__name {
    font-size: 60px;
    line-height: 1;
    font-weight: 300;
    letter-spacing: 1px;
  }
  .brand__sub {
    margin-top: 8px;
    font-size: 35px;
    line-height: 1;
    font-weight: 300;
  }

  .label {
    position: absolute;
    right: 412px;
    color: var(--gold-light);
    font-size: 37px;
    line-height: 1;
    text-align: right;
  }
  .label--services { top: 137px; }
  .label--products { top: 401px; }

  .list {
    position: absolute;
    left: 833px;
    list-style: none;
    color: var(--text);
    font-size: 28.5px;
    line-height: 38px;
    letter-spacing: 1.4px;
  }
  .list--services { top: 138px; }
  .list--products { top: 402px; }

  .hours {
    position: absolute;
    left: 0;
    width: 1200px;
    top: 581px;
    text-align: center;
    color: var(--gold);
    font-size: 30px;
    line-height: 1;
  }
</style>
</head>
<body>
<main class="card">
  <div class="rule rule--top"></div>

  <div class="brand">
    <svg class="brand__mark" width="120" height="120" viewBox="0 0 120 120" aria-hidden="true">
      <circle cx="60" cy="60" r="57" fill="none" stroke="var(--gold)" stroke-width="3"/>
    </svg>
    <div class="brand__name">Willowmere</div>
    <div class="brand__sub">Spa and Beauty Ltd.</div>
  </div>

  <div class="label label--services">Our services:</div>
  <ul class="list list--services">
    <li>Eyelash Extensions</li>
    <li>Manicures and Pedicures</li>
    <li>Body waxing</li>
    <li>Laser hair removal</li>
    <li>Injectable treatments</li>
    <li>Massages</li>
  </ul>

  <div class="label label--products">Pruducts:</div>
  <ul class="list list--products">
    <li>Skin cream serums,</li>
    <li>collagen gel, eye</li>
    <li>cream, etc.</li>
  </ul>

  <div class="rule rule--mid"></div>
  <p class="hours">Open 7days per week from 8am to 8pm.</p>
  <div class="rule rule--bottom"></div>
</main>
</body>
</html>
```